Whitcombe MD Crest Primary Care Business Card

Need a business card for a medical clinic targeting VIP patients. Should portray an upscale feeling. Simple, clean design. Logo and colors need to be incorporated into card. Clinic colors are gray/ silver, blues, white same as logo.
Clinic is a cash only VIP service clinic targeting higher income patients.
Tagline: "Where everyone is a VIP - Very Important Patient"

Target Market(s)

VIP, upscale

Industry/Entity Type

Medical

Contact Information for Business Card

Would like to use for cards with raised print or metallic highlight.

Requirements
Must have
• Incorporate logo, Use colors in logo
Nice to have
• Metallic detail
Should not have
• too much details or colors, other stock photos or designs

```html
<!DOCTYPE html>
<html lang="en">
<head>
<meta charset="utf-8">
<title>Whitcombe MD Crest Primary Care – Business Card</title>
<link href="https://fonts.googleapis.com/css2?family=Cinzel:wght@600&family=Lato:wght@400&family=PT+Sans:wght@400&display=swap" rel="stylesheet">
<style>
  :root {
    --backdrop: #e6e7ea;
    --paper: #fbfbfb;
    --navy: #2e4261;
    --slate: #4a5b72;
    --silver: #8e939a;
    --rule: #c9ccd1;
    --ink: #5a5f66;
    --white: #ffffff;
  }
  * { margin: 0; padding: 0; box-sizing: border-box; }
  html, body {
    width: 1200px; height: 844px; overflow: hidden;
    background: var(--backdrop);
  }
  .stage {
    position: relative; width: 1200px; height: 844px;
    display: flex; align-items: center; justify-content: center; gap: 50px;
  }
  .card {
    position: relative; width: 525px; height: 300px;
    box-shadow: 0 6px 18px rgba(0,0,0,.18);
  }
  /* Front */
  .card-front { background: var(--paper); }
  .brand {
    position: absolute; top: 62px; right: 30px;
    display: flex; align-items: center; gap: 10px;
  }
  .brand-dot {
    flex: none; width: 16px; height: 16px; border-radius: 50%;
    background: var(--navy);
  }
  .brand-name {
    font-family: "PT Sans", sans-serif; font-weight: 400;
    font-size: 17px; line-height: 1.3; color: var(--navy);
  }
  .divider {
    position: absolute; left: 28px; right: 28px; top: 150px;
    height: 1px; background: var(--rule);
  }
  .person { position: absolute; left: 30px; top: 170px; }
  .person-name {
    font-family: "Cinzel", serif; font-weight: 600; font-size: 17px;
    letter-spacing: .5px; color: var(--navy);
  }
  .person-name .surname { color: var(--silver); }
  .person-role, .address, .contact {
    font-family: "PT Sans", sans-serif; font-size: 13px; color: var(--ink);
  }
  .person-role { margin-top: 1px; }
  .address { position: absolute; left: 30px; top: 222px; }
  .contact-rule {
    position: absolute; left: 28px; right: 28px; top: 244px;
    height: 1px; background: var(--rule);
  }
  .contact { position: absolute; left: 30px; top: 252px; line-height: 1.35; }
  .contact .gap { margin-left: 10px; }
  .contact .web { color: var(--navy); margin-left: 10px; }
  /* Back */
  .card-back {
    background: var(--slate);
    display: flex; align-items: center; justify-content: center;
  }
  .tagline {
    font-family: "Lato", sans-serif; font-weight: 400; font-size: 27px;
    line-height: 1.45; color: var(--white); text-align: center;
    text-transform: uppercase; letter-spacing: .5px;
  }
</style>
</head>
<body>
<main class="stage">
  <section class="card card-front" aria-label="Card front">
    <div class="brand">
      <span class="brand-dot"></span>
      <div class="brand-name">Whitcombe MD<br>Crest Primary Care</div>
    </div>
    <div class="divider"></div>
    <div class="person">
      <div class="person-name">EVERETT <span class="surname">LANG</span></div>
      <div class="person-role">Managing Director</div>
    </div>
    <div class="address">12345, Address Goes Here Country Name, 123456.</div>
    <div class="contact-rule"></div>
    <div class="contact">
      <div>T:(044) 123 456 789<span class="gap">F:(044) 123456789</span><span class="gap">M:(044)123456789</span></div>
      <div>E:info@whitcombemd.com<span class="web">www.whitcombemd.com</span></div>
    </div>
  </section>
  <section class="card card-back" aria-label="Card back">
    <p class="tagline">Where everyone<br>is a VIP - Very<br>important patient</p>
  </section>
</main>
</body>
</html>
```